refresh/modernization of affiliate website template

Make this website look better. The site is comprised of various sections (nav, hero, products, FAQ, testimonials, gallery, contact us, blog listing page, single post page) that are modular in nature and it would be great if the genera template of the site was reusable with industries other than travel. We left the "look and feel" sliders in the neutral position because we are not too sure what we want and thus would like to see various approaches.

Number of Pages Required

3 page

```html
<!DOCTYPE html>
<html lang="en">
<head>
<meta charset="utf-8">
<title>Contact Us – Maple Harbor</title>
<link href="https://fonts.googleapis.com/css2?family=Montserrat:wght@400;500;600;700&display=swap" rel="stylesheet">
<style>
  :root {
    --green: #0a9b3b;
    --lime: #b1ca2a;
    --ink: #333333;
    --text: #444444;
    --muted: #666666;
    --hero-bg: #eff1f0;
    --footer-bg: #363435;
    --footer-line: #555355;
    --rule: #e3e3e3;
    --white: #ffffff;
  }
  * { box-sizing: border-box; margin: 0; padding: 0; }
  html, body { width: 1049px; height: 1200px; overflow: hidden; background: var(--white); }
  body { position: relative; font-family: "Montserrat", sans-serif; color: var(--text); }
  .abs { position: absolute; }
  a { color: inherit; text-decoration: none; }

  /* Top bar */
  .topbar { left: 0; top: 0; width: 1049px; height: 86px; border-bottom: 1px solid var(--rule); }
  .social { left: 125px; top: 31px; display: flex; gap: 6px; }
  .social span { width: 28px; height: 28px; border-radius: 50%; background: var(--green); display: block; }
  .brand { left: 0; width: 1049px; top: 32px; text-align: center; font-weight: 600; font-size: 20px; line-height: 24px; color: var(--ink); }
  .top-mail { left: 714px; top: 29px; display: flex; align-items: center; gap: 8px; font-size: 13.5px; color: var(--text); }
  .icon-circle { border-radius: 50%; background: var(--green); display: flex; align-items: center; justify-content: center; flex: none; }

  /* Nav */
  .nav { left: 0; top: 86px; width: 1049px; height: 47px; border-bottom: 1px solid var(--rule); }
  .nav a { position: absolute; top: 15px; font-size: 13px; color: var(--ink); letter-spacing: 0.2px; }
  .nav a.active { font-weight: 700; }
  .nav .underline { position: absolute; left: 99px; top: 44px; width: 68px; height: 3px; background: var(--green); }

  /* Hero */
  .hero { left: 0; top: 133px; width: 1049px; height: 260px; background: var(--hero-bg); }
  .hero-kicker { left: 0; width: 1049px; top: 85px; text-align: center; font-weight: 700; font-size: 23px; color: var(--green); }
  .hero-title { left: 0; width: 1049px; top: 110px; text-align: center; font-weight: 700; font-size: 38px; color: var(--ink); }

  /* Contact information */
  .info-title { left: 121px; top: 464px; font-weight: 700; font-size: 26px; color: var(--ink); }
  .divider { left: 125px; top: 502px; display: flex; align-items: center; gap: 8px; }
  .divider i { display: block; width: 43px; height: 1px; background: #bbbbbb; }
  .divider b { display: block; width: 14px; height: 14px; background: var(--lime); }
  .info-text { left: 125px; top: 530px; width: 335px; font-size: 11px; line-height: 18.2px; color: var(--text); }
  .info-item { display: flex; align-items: center; gap: 9px; }
  .info-item .label { font-size: 10.5px; color: var(--muted); }
  .info-item .value { font-size: 16.5px; font-weight: 600; color: var(--ink); margin-top: 2px; }
  .phone-item { left: 123px; top: 608px; }
  .mail-item { left: 127px; top: 688px; }

  /* Form */
  .form-edge { left: 532px; top: 465px; width: 414px; height: 328px; border: 2.5px solid var(--green); border-radius: 0 54px 0 54px; }
  .form-card { left: 524px; top: 455px; width: 412px; height: 327px; background: var(--lime); border-radius: 0 54px 0 54px; }
  .field { position: absolute; left: 37px; width: 327px; border-bottom: 1.5px solid var(--white); color: var(--white); font-size: 13px; font-weight: 500; }
  .submit { position: absolute; left: 33px; top: 255px; width: 121px; height: 32px; border-radius: 16px; background: var(--green); color: var(--white); font-weight: 700; font-size: 12px; display: flex; align-items: center; justify-content: center; letter-spacing: 0.3px; }

  .to-top { left: 944px; top: 859px; width: 35px; height: 35px; border-radius: 50%; background: var(--lime); display: flex; align-items: center; justify-content: center; z-index: 2; }

  /* Footer */
  .footer { left: 0; top: 878px; width: 1049px; height: 322px; background: var(--footer-bg); color: var(--white); }
  .col-line { position: absolute; top: 0; width: 1px; height: 214px; background: var(--footer-line); }
  .col-bar { position: absolute; top: 58px; width: 3px; height: 21px; background: var(--white); }
  .foot-brand { left: 120px; top: 66px; font-weight: 600; font-size: 20px; line-height: 24px; color: var(--white); }
  .foot-about { left: 118px; top: 114px; width: 200px; font-size: 8.8px; line-height: 12.2px; color: #dddddd; }
  .copyright { left: 118px; top: 167px; font-size: 8.8px; color: #dddddd; }
  .copyright u { color: var(--white); }
  .foot-head { font-weight: 700; font-size: 11.5px; letter-spacing: 0.2px; }
  .quick-links { left: 390px; top: 89px; list-style: none; font-size: 10px; }
  .quick-links li { height: 22.6px; }
  .foot-social { left: 550px; top: 88px; display: flex; gap: 4px; }
  .foot-social span { width: 23px; height: 23px; border-radius: 50%; background: var(--white); display: block; }
  .foot-mail { left: 549px; top: 126px; display: flex; align-items: center; gap: 6px; font-size: 10px; line-height: 14px; }
  .sub-input { left: 749px; top: 84px; width: 176px; height: 30px; background: var(--white); border-radius: 2px; color: var(--muted); font-size: 9.5px; padding: 8px 14px; }
  .sub-btn { left: 749px; top: 121px; width: 176px; height: 30px; background: var(--green); border-radius: 2px; font-weight: 700; font-size: 9.5px; display: flex; align-items: center; justify-content: center; }
</style>
</head>
<body>

<header class="abs topbar">
  <div class="abs social" aria-label="Social links"><span></span><span></span><span></span><span></span></div>
  <div class="abs brand">Maple Harbor</div>
  <div class="abs top-mail">
    <span class="icon-circle" style="width:30px;height:30px">
      <svg width="16" height="12" viewBox="0 0 16 12"><rect x="0.75" y="0.75" width="14.5" height="10.5" fill="none" stroke="#fff" stroke-width="1.5"/><path d="M1 1l7 6 7-6M1 11l5-5M15 11l-5-5" fill="none" stroke="#fff" stroke-width="1.3"/></svg>
    </span>
    hello@mapleharbor.com
  </div>
</header>

<nav class="abs nav">
  <a class="active" style="left:113px">HOME</a>
  <a style="left:244px">PRODUCTS DEALS</a>
  <a style="left:449px">BLOGS</a>
  <a style="left:578px">TESTIMONIALS</a>
  <a style="left:760px">FAQ</a>
  <a style="left:871px">CONTACT</a>
  <span class="underline"></span>
</nav>

<section class="abs hero" role="img" aria-label="Light grey banner with a faint geometric line pattern">
  <p class="abs hero-kicker">GET IN TOUCH WITH US</p>
  <h1 class="abs hero-title">CONTACT US</h1>
</section>

<section>
  <h2 class="abs info-title">CONTACT INFORMATION</h2>
  <div class="abs divider"><i></i><b></b><i></i></div>
  <p class="abs info-text">Lorem ipsum dolor sit amet, consectetur adipiscing elit, sed do eiusmod tempor incididunt ut labore et dolore magna aliqua. Ut enim ad minim veniam, quis</p>

  <div class="abs info-item phone-item">
    <span class="icon-circle" style="width:45px;height:45px">
      <svg width="20" height="26" viewBox="0 0 20 26"><path d="M10 1a9 9 0 0 0-9 9c0 6.5 9 15 9 15s9-8.5 9-15a9 9 0 0 0-9-9z" fill="#fff"/><circle cx="10" cy="10" r="3.4" fill="#0a9b3b"/></svg>
    </span>
    <div><div class="label">Phone Number</div><div class="value">(555) 014-2290</div></div>
  </div>

  <div class="abs info-item mail-item">
    <span class="icon-circle" style="width:45px;height:45px">
      <svg width="26" height="19" viewBox="0 0 26 19"><rect x="1" y="1" width="24" height="17" fill="none" stroke="#fff" stroke-width="2"/><path d="M1.5 1.5L13 11 24.5 1.5M1.5 17.5l8.5-8.5M24.5 17.5L16 9" fill="none" stroke="#fff" stroke-width="2"/></svg>
    </span>
    <div><div class="label">Email address</div><div class="value">info@yourcompany.com</div></div>
  </div>

  <div class="abs form-edge"></div>
  <form class="abs form-card">
    <div class="field" style="top:44px;height:22px">Name</div>
    <div class="field" style="top:87px;height:29px">Email address</div>
    <div class="field" style="top:130px;height:25px">Phone number</div>
    <div class="field" style="top:173px;height:63px">Message</div>
    <div class="submit">SUBMIT</div>
  </form>
</section>

<a class="abs to-top" aria-label="Back to top">
  <svg width="14" height="18" viewBox="0 0 14 18"><path d="M7 17V2M1 8l6-6 6 6" fill="none" stroke="#fff" stroke-width="1.8"/></svg>
</a>

<footer class="abs footer">
  <span class="col-line" style="left:364px"></span>
  <span class="col-line" style="left:524px"></span>
  <span class="col-line" style="left:725px"></span>
  <span class="col-bar" style="left:364px"></span>
  <span class="col-bar" style="left:524px"></span>
  <span class="col-bar" style="left:725px"></span>

  <div class="abs foot-brand">Maple Harbor</div>
  <p class="abs foot-about">Lorem ipsum dolor sit amet, consectetur adipiscing elit, sed do eiusmod tempor incididunt ut labore et dolore</p>
  <p class="abs copyright">© 2022 <u>MapleHarbor</u>. All Rights Reserved</p>

  <h3 class="abs foot-head" style="left:387px;top:61px">QUICK LINKS</h3>
  <ul class="abs quick-links">
    <li>Home</li><li>Products</li><li>FAQ</li><li>Blogs</li><li>Testimonials</li><li>Contact Us</li>
  </ul>

  <h3 class="abs foot-head" style="left:550px;top:61px">GET IN TOUCH</h3>
  <div class="abs foot-social" aria-label="Social links"><span></span><span></span><span></span><span></span></div>
  <div class="abs foot-mail">
    <span class="icon-circle" style="width:25px;height:25px;background:#fff">
      <svg width="13" height="10" viewBox="0 0 13 10"><rect x="0.6" y="0.6" width="11.8" height="8.8" fill="none" stroke="#363435" stroke-width="1.2"/><path d="M1 1l5.5 4.5L12 1" fill="none" stroke="#363435" stroke-width="1.2"/></svg>
    </span>
    <div><strong>Email address</strong><br>info@yourcompany.com</div>
  </div>

  <h3 class="abs foot-head" style="left:748px;top:61px">SUBSCRIBE FOR DEALS</h3>
  <div class="abs sub-input">Email address</div>
  <div class="abs sub-btn">SUBSCRIBE</div>
</footer>

</body>
</html>
```